Lumen Haven Centers and Experiences

This is a Pitch Deck to show to investors and partners.

This project is focused on creating unique Co-Living Retreat Centers focused on building community and optimal living.

All the content is in the folder provided below.

https://files.varodesk.com/folders/8KpR2zTnWqY4vLmXcBeHjDa93sFgNuVoAtQ?usp=sharing

Target Market(s)

Majority 30-50 years of age. smaller subsets (20-30 and 50-60)
People that have high regard for growth in all areas of life.
People that have worked really hard and are facing burnout and looking for more balance, joy, happiness and meaning.
Yoga, Meditation, Surfing, Co-Working, Hiking, Adventure, Masterminds,

Font styles to use
Sans Serif

Colors

Designer to choose colors to be used in the design.

Requirements
Must have
• I would like to have a slight bit of gold colour in the designs.
Nice to have
• Professional and clean, with a focus on sustainability and futuristic living. Maybe slight use of sacred geometry
Should not have
• I am open to suggestions on the content, If you feel like the written content should be reduced for the designs sake.

```html
<!DOCTYPE html>
<html lang="en">
<head>
<meta charset="utf-8">
<title>Lumen Haven – Investor Deck Overview</title>
<link href="https://fonts.googleapis.com/css2?family=Montserrat:wght@300;400&family=Questrial&display=swap" rel="stylesheet">
<style>
:root{
  --gold:#f6c21c;
  --gold-soft:#fde9a0;
  --ink:#3b3b3b;
  --muted:#6e6e6e;
  --line:#bdbdbd;
  --ring:#e2e2e2;
  --paper:#ffffff;
  --night:#000000;
  --brand-blue:#2b8bcf;
}
*{box-sizing:border-box}
html,body{margin:0;padding:0;width:1200px;height:963px;overflow:hidden;background:var(--night)}
.deck{position:relative;width:1200px;height:963px}
.slide{position:absolute;background:var(--paper);overflow:hidden;font-family:"Questrial",sans-serif;color:var(--ink);line-height:1.2}
.lg{width:320px;height:179px;top:23px}
.sm{width:268px;height:151px}
.c1{left:45px}.c2{left:326px}.c3{left:606px}.c4{left:887px}
.r2{top:225px}.r3{top:413px}.r4{top:601px}.r5{top:789px}
.abs{position:absolute}
.photo{position:absolute}
.accent-bar{position:absolute;right:0;top:36px;width:8px;height:78px;background:var(--gold)}
.lg .accent-bar{top:44px;height:90px;right:3px}
.heading{position:absolute;margin:0;font-family:"Questrial",sans-serif;font-weight:400;font-variant:small-caps;letter-spacing:.09em;color:#2e2e2e}
.center{text-align:center}
.tags{position:absolute;left:0;right:0;text-align:center;white-space:nowrap}
.tag{display:inline-block;border:.6px solid #8a8a8a;border-radius:2px;padding:.4px 2px;margin:0 .8px;font-size:3.6px;color:#555}
.lg .tag{font-size:4.6px;padding:.6px 2.4px}
.dash{position:absolute;height:.7px;background:#444}
p{margin:0}

/* cover */
.cover-title{position:absolute;left:150px;top:36px;width:160px;margin:0;text-align:center;font-family:"Montserrat",sans-serif;font-weight:300;font-size:19px;letter-spacing:.04em;color:#fff}
.cover-rule{position:absolute;left:216px;top:66px;width:46px;height:1.2px;background:#fff}
.cover-sub{position:absolute;left:150px;top:88px;width:160px;text-align:center;font-family:"Montserrat",sans-serif;font-weight:300;font-size:8.2px;line-height:10.2px;color:#fff}

/* cards */
.card{position:absolute;border:1px solid var(--gold);border-radius:4px;text-align:center}
.card .icon{position:absolute;left:50%;top:-12px;margin-left:-10px;width:20px;height:20px;border-radius:50%;background:#fff;border:1px solid var(--gold)}
.card .icon::after{content:"";position:absolute;left:6px;top:6px;width:6px;height:6px;border-radius:50%;border:.8px solid #555}
.card h3{margin:9px 0 1px;font-weight:400;font-size:4.4px;color:#333}
.card p{margin:0 3px;font-size:2.8px;line-height:3.2px;color:#555}

/* team */
.member{position:absolute;width:42px;text-align:center;font-size:3.3px;line-height:3.8px;color:#555}
.avatar{width:26px;height:26px;margin:0 auto 3px;border-radius:50%;border:1px solid var(--gold);background:radial-gradient(circle at 50% 40%,#b8a595,#5a4a40)}

/* experience */
.brand{position:absolute;width:92px}
.brand-mark{position:absolute;left:0;top:0;width:21px;height:21px;border-radius:50%;background:var(--brand-blue)}
.brand h4{position:absolute;left:27px;top:0;width:62px;margin:0;font-weight:400;font-size:5.6px;color:#333;border-bottom:.7px solid var(--gold);padding-bottom:1px}
.brand p{position:absolute;left:27px;top:10px;width:64px;font-size:3px;line-height:3.5px;color:#555}

/* partners */
.partner{position:absolute;transform:translateX(-50%);font-size:4.6px;letter-spacing:.05em;color:#222;white-space:nowrap}

/* venn */
.venn{position:absolute;width:56px;height:56px;border-radius:50%;border:.8px solid var(--line);display:flex;align-items:center;justify-content:center;text-align:center;font-size:4.4px;line-height:5.2px;color:#444}
.pill{position:absolute;background:var(--gold);border:.6px solid #b58d00;border-radius:3px;font-size:4.2px;padding:.6px 3px;color:#333;white-space:nowrap}

/* hexagons */
.hex{position:absolute;clip-path:polygon(25% 0,75% 0,100% 50%,75% 100%,25% 100%,0 50%);display:flex;align-items:center;justify-content:center;text-align:center}
.hex.gold{background:var(--gold);color:#333}
.hex.grey{background:#e3e3e3;color:#555}

/* governance */
.level{position:absolute;border:.7px solid #888;border-radius:2px;font-size:4.4px;padding:.4px 4px;background:#fff;color:#333}
.level-note{position:absolute;font-size:3px;line-height:3.5px;color:#555}

/* sustainability */
.pillar-icon{position:absolute;left:96px;width:20px;height:20px;border-radius:50%;border:1.2px solid var(--gold);background:#fff}
.pillar-title{position:absolute;left:119px;font-size:5.6px;color:#333}
.pillar-box{position:absolute;left:104px;width:145px;height:22px;border:1px solid var(--gold);border-radius:4px;padding:4px 5px 0 14px;font-size:3.5px;line-height:4px;color:#444}

/* timeline */
.tl-year{position:absolute;top:32px;font-size:6px;color:#333}
.tl-dot{position:absolute;top:42.5px;width:5px;height:5px;border-radius:50%;background:#333}
.tl-col{position:absolute;top:56px;width:80px;font-size:3px;line-height:3.4px;color:#444}
.tl-col b{font-weight:400;display:block;margin-top:2.4px}

/* funding */
.fund-text{position:absolute;left:8px;top:32px;width:80px;font-size:2.9px;line-height:3.3px;color:#444;text-align:justify}
.fund-text p{margin-bottom:2.4px}
.returns{position:absolute;left:93px;top:36px;width:163px;border-collapse:collapse;font-size:2.6px;color:#444}
.returns td{border:.3px solid #bbb;padding:.6px 1px;text-align:center;height:4.6px}
.returns .blank{border:none}
</style>
</head>
<body>
<main class="deck">

<!-- Cover -->
<section class="slide lg" style="left:274px">
  <div class="photo" role="img" aria-label="Palm trees silhouetted on a beach at sunset" style="inset:0;background:linear-gradient(180deg,#293150 0%,#45425d 38%,#8f6650 70%,#c88a4c 82%,#2c2220 100%)"></div>
  <h1 class="cover-title">LUMEN HAVEN</h1>
  <div class="cover-rule"></div>
  <p class="cover-sub">A network of crowdfunded<br>sustainable co-living retreat<br>centres around the world,<br>focused on optimal living!</p>
  <div class="accent-bar"></div>
</section>

<!-- Mission -->
<section class="slide lg" style="left:607px">
  <p class="abs center" style="left:8px;top:34px;width:110px;font-size:6.1px;line-height:8px;color:#444">We are enabling our network of communities to co-own these spaces. Utilizing our collective intelligence and a financial model that enables everyone to reap the benefits of co-investing and growing incredible physical spaces together.</p>
  <div class="dash" style="left:55px;top:107px;width:14px"></div>
  <div class="tags" style="width:125px;top:125px"><span class="tag">Biohacking</span><span class="tag">Meditation</span><span class="tag">Nature</span></div>
  <div class="tags" style="width:125px;top:137px"><span class="tag">Inspiring Workspaces</span><span class="tag">Yoga</span><span class="tag">Spa's</span></div>
  <div class="tags" style="width:125px;top:149px"><span class="tag">Masterminds</span><span class="tag">Float Tanks</span><span class="tag">Cold Plunges</span></div>
  <div class="photo" role="img" aria-label="Bamboo lounge with teal sofas and hanging lanterns in a tropical garden" style="left:125px;top:0;width:195px;height:179px;background:linear-gradient(160deg,#7c8a6a 0%,#5c5142 35%,#2f8a8a 60%,#4a3a2c 100%)"></div>
  <div class="accent-bar"></div>
</section>

<!-- Audience -->
<section class="slide sm c1 r2">
  <div class="photo" role="img" aria-label="Bamboo structure detail" style="left:0;top:0;width:15px;height:151px;background:linear-gradient(180deg,#8a6a44,#5b4128)"></div>
  <p class="abs center" style="left:19px;top:27px;width:111px;font-size:5px;line-height:6px;color:#444">These spaces are created for people that are seeking more depth, meaning, balance, joy and impact in their life.</p>
  <div class="dash" style="left:69px;top:53px;width:12px"></div>
  <p class="abs center" style="left:19px;top:68px;width:111px;font-size:5px;line-height:6px;color:#444">Targeting people that already have communities and can run their own events and retreats:</p>
  <div class="tags" style="width:149px;top:95px"><span class="tag">Experience Creators</span><span class="tag">Facilitators</span><span class="tag">Yoga Teachers</span></div>
  <div class="tags" style="width:149px;top:108px"><span class="tag">Coaches</span><span class="tag">Entrepreneurs</span><span class="tag">Musicians</span><span class="tag">Artists</span></div>
  <div class="tags" style="width:149px;top:121px"><span class="tag">Digital Nomads</span><span class="tag">Social Impact Investors</span></div>
  <div class="photo" role="img" aria-label="Woven bamboo arch framing a view of a forest" style="left:134px;top:0;width:134px;height:151px;background:linear-gradient(180deg,#b48a52 0%,#8c6438 50%,#3f4a2c 100%)"></div>
  <div class="accent-bar"></div>
</section>

<!-- Rooms and facilities -->
<section class="slide sm c2 r2">
  <p class="abs center" style="left:0;top:30px;width:118px;font-size:5.4px;color:#444">Each property has <span style="font-size:7.6px">30 rooms</span></p>
  <p class="abs center" style="left:0;top:40px;width:118px;font-size:7px;color:#444">15 Rooms <span style="font-size:4.8px">for Co-Living</span></p>
  <p class="abs center" style="left:0;top:49px;width:118px;font-size:7px;color:#444">15 Rooms <span style="font-size:4.8px">for the Retreat Center</span></p>
  <p class="abs center" style="left:0;top:76px;width:118px;font-size:7px;color:#444">Facilities</p>
  <div class="tags" style="width:118px;top:93px"><span class="tag">Pool</span><span class="tag">Yoga Shala's</span><span class="tag">Ice Bath</span><span class="tag">Sauna</span></div>
  <div class="tags" style="width:118px;top:104px"><span class="tag">Steam Room</span><span class="tag">Work Space</span><span class="tag">Common Areas</span></div>
  <div class="tags" style="width:118px;top:116px"><span class="tag">Fitness Center</span><span class="tag">Nature</span><span class="tag">Other Biohacking Tools</span></div>
  <div class="photo" role="img" aria-label="Infinity pool among palm trees" style="left:118px;top:5px;width:150px;height:42px;background:linear-gradient(180deg,#a9c6b8,#3f8fa0)"></div>
  <div class="photo" role="img" aria-label="Bamboo hall interior" style="left:118px;top:49px;width:60px;height:47px;background:linear-gradient(180deg,#a47a44,#5a3f22)"></div>
  <div class="photo" role="img" aria-label="Open-air yoga pavilion in the forest" style="left:118px;top:98px;width:60px;height:25px;background:linear-gradient(180deg,#6f7a52,#3f3a2a)"></div>
  <div class="photo" role="img" aria-label="Warm lit bamboo lounge" style="left:118px;top:125px;width:60px;height:26px;background:linear-gradient(180deg,#8a5a30,#3a2516)"></div>
  <div class="photo" role="img" aria-label="Bedroom with canopy bed under a bamboo roof" style="left:180px;top:49px;width:88px;height:102px;background:linear-gradient(180deg,#b79266 0%,#e8e2d8 55%,#d8d0c4 100%)"></div>
  <div class="accent-bar"></div>
</section>

<!-- First project -->
<section class="slide sm c3 r2">
  <p class="abs center" style="left:0;top:17px;width:260px;font-size:7px;color:#333">FIRST PROJECT</p>
  <p class="abs center" style="left:0;top:31px;width:260px;font-size:5.4px;line-height:7.2px;color:#444">Bali<br>1.5 Acres of Land<br>25 year Lease (option to extend) - $400,000<br>Build Costs - $1,100,000</p>
  <p class="abs center" style="left:0;top:80px;width:260px;font-size:7px;color:#333">FUTURE LOCATIONS</p>
  <div class="photo" role="img" aria-label="Costa Rica coastline" style="left:51px;top:96px;width:25px;height:25px;background:linear-gradient(180deg,#5f8a4a,#2f5a36)"></div>
  <div class="photo" role="img" aria-label="Hawaii cliffs and ocean" style="left:86px;top:96px;width:25px;height:25px;background:linear-gradient(180deg,#7aa6c8,#3d6a4a)"></div>
  <div class="photo" role="img" aria-label="Philippines lagoon" style="left:122px;top:96px;width:25px;height:25px;background:linear-gradient(180deg,#4fb0c8,#2e6d5a)"></div>
  <div class="photo" role="img" aria-label="Portugal coastal town" style="left:159px;top:96px;width:25px;height:25px;background:linear-gradient(180deg,#8fb8d8,#a46a4a)"></div>
  <div class="photo" role="img" aria-label="Uruguay beach" style="left:194px;top:96px;width:25px;height:25px;background:linear-gradient(180deg,#a8cfe6,#d8cbb0)"></div>
  <p class="abs center" style="left:44px;top:124px;width:39px;font-size:4.8px">Costa Rica</p>
  <p class="abs center" style="left:79px;top:124px;width:39px;font-size:4.8px">Hawaii</p>
  <p class="abs center" style="left:115px;top:124px;width:39px;font-size:4.8px">Philippines</p>
  <p class="abs center" style="left:152px;top:124px;width:39px;font-size:4.8px">Portugal</p>
  <p class="abs center" style="left:187px;top:124px;width:39px;font-size:4.8px">Uruguay</p>
  <div class="accent-bar"></div>
</section>

<!-- Products -->
<section class="slide sm c4 r2">
  <p class="abs center" style="left:30px;top:11px;width:208px;font-size:3.7px;line-height:4.4px;color:#555">In order to create a strong community of people seeking this lifestyle we will create a number of different products to reach the masses and give them a taste of what its like to have a likeminded community</p>
  <div class="card" style="left:13px;top:45px;width:78px;height:40px"><span class="icon"></span><h3>Online Courses</h3><p>Jumpstart strategy to reach masses with easily accessible programs. Providing people with knowledge on a wide array of personal development topics.</p></div>
  <div class="card" style="left:96px;top:45px;width:78px;height:40px"><span class="icon"></span><h3>Local Events</h3><p>Building local communities and inspiring people through speakers and workshops. Creating a desire to dive deeper into personal development and engage more with the community.</p></div>
  <div class="card" style="left:179px;top:45px;width:78px;height:40px"><span class="icon"></span><h3>Global Experiences</h3><p>Transformational retreats and tours that provide meaningful in depth travel experiences that focus on personal growth, health and wellness, integrating local culture, giving back to the community.</p></div>
  <div class="card" style="left:13px;top:100px;width:78px;height:40px"><span class="icon"></span><h3>Havenfests</h3><p>Tailored as a hybrid of many other well-known events; with hints of Dust Fest, Idea Talks, Ridge Series, and Sun Fest combined together in unique environments.</p></div>
  <div class="card" style="left:96px;top:100px;width:78px;height:40px"><span class="icon"></span><h3>Media</h3><p>Releasing Viral Content that inspires people and reaches the masses, building interest in our community.</p></div>
  <div class="card" style="left:179px;top:100px;width:78px;height:40px"><span class="icon"></span><h3>Influencers</h3><p>Using the power of influencer marketing to reach large targeted communities.</p></div>
</section>

<!-- Havenfests -->
<section class="slide sm c1 r3">
  <div class="photo" role="img" aria-label="Group sitting in a circle on a tropical beach" style="left:0;top:0;width:115px;height:151px;background:linear-gradient(180deg,#7fb4c4 0%,#c9b48e 45%,#a37e5e 100%)"></div>
  <h2 class="heading" style="left:121px;top:8px;font-size:10px;letter-spacing:.14em">HAVENFESTS</h2>
  <div class="abs" style="left:121px;top:26px;width:134px;font-size:3px;line-height:3.5px;color:#555">
    <p style="margin-bottom:2px">To create awareness and build our community of investors we will launch mini festivals co-created by our partners and facilitators. Each partner company will sell it to their network bringing together all the different communities to create a larger community. The focus will be on creating peak life changing experiences through all different types of modalities.</p>
    <p style="margin-bottom:2px">All profits will go towards building or acquiring the space. A % of ownership will be provided to all partner companies based on their ticket sales and the quality of experience they provide.</p>
    <p style="margin-bottom:2px">All attendee's will have the opportunity to invest into the Lumen Haven properties and stay engaged in their new community!</p>
    <p>We will utilize existing infrastructure from our previous company.</p>
  </div>
  <div class="abs" style="left:121px;top:94px;width:135px;height:.6px;background:#888"></div>
  <p class="abs center" style="left:121px;top:103px;width:52px;font-size:3.3px;line-height:3.9px;color:#555">March 2021<br>Island Havenfest<br>Private Island in Panama<br>300-500 people<br>Glamping<br>High End Dining</p>
  <div class="abs" style="left:186px;top:105px;width:.6px;height:24px;background:#555"></div>
  <p class="abs center" style="left:196px;top:103px;width:60px;font-size:3.3px;line-height:3.9px;color:#555">August 2021<br>Croatia Havenfest<br>5-10 Yachts (40 pax per yacht)<br>7 Different Islands<br>Top level speakers and facilitators</p>
  <div class="accent-bar"></div>
</section>

<!-- Team -->
<section class="slide sm c2 r3">
  <h2 class="heading" style="left:18px;top:12px;font-size:12px">The Team</h2>
  <div class="member" style="left:14px;top:35px"><div class="avatar" role="img" aria-label="Portrait placeholder"></div>Rowan Tellis<br>Founder</div>
  <div class="member" style="left:54px;top:35px"><div class="avatar" role="img" aria-label="Portrait placeholder"></div>Marlo Quint<br>Finance/Operations</div>
  <div class="member" style="left:94px;top:35px"><div class="avatar" role="img" aria-label="Portrait placeholder"></div>Tessa Varlow<br>Local Events</div>
  <div class="member" style="left:134px;top:35px"><div class="avatar" role="img" aria-label="Portrait placeholder"></div>Nadia Orsk<br>Global Events</div>
  <div class="member" style="left:175px;top:35px"><div class="avatar" role="img" aria-label="Portrait placeholder"></div>Cole Barrin<br>Transformational Travel</div>
  <div class="member" style="left:215px;top:35px"><div class="avatar" role="img" aria-label="Portrait placeholder"></div>Arjun Pelle<br>Sustainable Building and Developer</div>
  <div class="member" style="left:14px;top:89px"><div class="avatar" role="img" aria-label="Portrait placeholder"></div>Dario Lenz<br>Partnerships/ Sponsorships/Media</div>
  <div class="member" style="left:54px;top:89px"><div class="avatar" role="img" aria-label="Portrait placeholder"></div>Owen Tarrow<br>Development/ Funding</div>
  <div class="member" style="left:94px;top:89px"><div class="avatar" role="img" aria-label="Portrait placeholder"></div>Evan Holt<br>Real Estate/Events</div>
  <div class="member" style="left:134px;top:89px"><div class="avatar" role="img" aria-label="Portrait placeholder"></div>Silas Brenner<br>Blockchain</div>
  <div class="member" style="left:175px;top:89px"><div class="avatar" role="img" aria-label="Portrait placeholder"></div>Luca Fenwick<br>Overland</div>
  <div class="member" style="left:215px;top:89px"><div class="avatar" role="img" aria-label="Portrait placeholder"></div>Reid Caldow<br>Changemakers</div>
  <div class="abs" style="left:134px;top:84px;width:1.4px;height:56px;background:var(--gold)"></div>
  <div class="abs" style="left:134px;top:84px;width:122px;height:1.4px;background:var(--gold)"></div>
  <h3 class="heading" style="left:160px;top:136px;width:72px;text-align:center;font-size:8px">Advisors</h3>
  <div class="accent-bar"></div>
</section>

<!-- Experience -->
<section class="slide sm c3 r3">
  <h2 class="heading" style="left:13px;top:15px;font-size:12px">Experience</h2>
  <p class="abs" style="left:13px;top:34px;font-size:3.8px;color:#555">Rowan has 13 years of experience in the travel industry founding these brands:</p>
  <div class="abs" role="img" aria-label="Portrait placeholder" style="left:204px;top:6px;width:49px;height:49px;border-radius:50%;border:1.5px solid var(--gold);background:radial-gradient(circle at 50% 40%,#c9b4a2,#6a5446)"></div>
  <p class="abs center" style="left:194px;top:59px;width:69px;font-size:5.4px;color:#333">Rowan Tellis</p>
  <div class="brand" style="left:13px;top:44px"><span class="brand-mark"></span><h4>Open Road Years</h4><p>Tour Company operating in 18 different countries.</p></div>
  <div class="brand" style="left:107px;top:44px"><span class="brand-mark"></span><h4>DriftHouse</h4><p>A Co-Living space in Nicaragua hosting up to 35 guests at a time.</p></div>
  <div class="brand" style="left:13px;top:72px"><span class="brand-mark"></span><h4>Isleward</h4><p>A mini festival on a private island in Panama focused on personal growth.</p></div>
  <div class="brand" style="left:107px;top:72px"><span class="brand-mark"></span><h4>Cliffside Homestay</h4><p>A 10 room hotel and yoga retreat centre.</p></div>
  <div class="brand" style="left:13px;top:101px"><span class="brand-mark"></span><h4>StillMat</h4><p>Yoga Retreats in Thailand</p></div>
  <div class="brand" style="left:107px;top:101px"><span class="brand-mark"></span><h4>SailCircle</h4><p>Sailing experiences in Croatia, Turkey and Greece.</p></div>
  <p class="abs" style="left:13px;top:130px;width:212px;font-size:3.7px;line-height:4.4px;color:#555">He is now shifting his focus to create a more sustainable way of life, utilizing his experience in travel and Co-Living to build these communities around the world with the intention of creating a positive impact on the world!</p>
  <div class="accent-bar"></div>
</section>

<!-- Partners -->
<section class="slide sm c4 r3">
  <h2 class="heading center" style="left:0;top:14px;width:268px;font-size:11px">Our Experience Partners</h2>
  <span class="partner" style="left:44px;top:58px">CADENCE COLLECTIVE</span>
  <span class="partner" style="left:94px;top:58px">WAYFARER</span>
  <span class="partner" style="left:163px;top:58px">RENEW RETREATS</span>
  <span class="partner" style="left:218px;top:58px">AURORA PATH</span>
  <span class="partner" style="left:24px;top:88px">FAR &amp; NEAR</span>
  <span class="partner" style="left:97px;top:88px">OFFBEAT LIVING</span>
  <span class="partner" style="left:155px;top:88px">REBOUND</span>
  <span class="partner" style="left:198px;top:88px">OVERLAND</span>
  <span class="partner" style="left:241px;top:88px">PATHFINDER</span>
  <span class="partner" style="left:33px;top:116px">KINDLED</span>
  <span class="partner" style="left:98px;top:116px">BREATH RISING</span>
  <span class="partner" style="left:172px;top:116px">SUMMIT MINDS</span>
  <span class="partner" style="left:234px;top:116px">TIDEBREATH</span>
  <div class="accent-bar"></div>
</section>

<!-- Industries -->
<section class="slide sm c1 r4">
  <div class="photo" role="img" aria-label="Glowing geodesic dome tent at dusk" style="left:0;top:0;width:95px;height:151px;background:linear-gradient(180deg,#c9c4bc 0%,#e0a04a 45%,#7a4a22 100%)"></div>
  <p class="abs" style="left:112px;top:20px;width:135px;font-size:5px;line-height:6px;color:#444">We are tapping into 3 trending industries at the same time:</p>
  <div class="venn" style="left:155px;top:33px">Kindred Rooms<br>Gatherhall<br>Roamhold<br>Nestmore</div>
  <div class="venn" style="left:126px;top:89px">Solstice Gather<br>Peakline<br>Tidal Circle</div>
  <div class="venn" style="left:183px;top:89px">InnerArc<br>Learnwell<br>Openfield Academy</div>
  <span class="pill" style="left:195px;top:41px">Co-Living</span>
  <span class="pill" style="left:106px;top:128px">Events/Retreats</span>
  <span class="pill" style="left:211px;top:128px">Online Courses</span>
  <div class="accent-bar"></div>
</section>

<!-- Market trends -->
<section class="slide sm c2 r4">
  <h2 class="heading" style="left:14px;top:14px;font-size:12px;line-height:14px">Market<br>Trends</h2>
  <div class="hex" role="img" aria-label="People meditating in a round hall" style="left:83px;top:18px;width:56px;height:48px;background:linear-gradient(180deg,#b76a44,#5a3424)"></div>
  <div class="hex grey" style="left:156px;top:23px;width:50px;height:44px"><span style="font-size:3.1px;line-height:3.6px;padding:0 5px">Personal Development expected to grow from 9.9 Billion to 13 Billion by 2022***</span></div>
  <div class="hex" role="img" aria-label="Person standing at sunset" style="left:51px;top:44px;width:40px;height:35px;background:linear-gradient(180deg,#e0945a,#6a4a3a)"></div>
  <div class="hex gold" style="left:129px;top:53px;width:40px;height:35px"><span style="font-size:2.4px;line-height:2.9px;padding:0 5px">E-Learning is forecast to surpass 243 billion U.S. dollars by 2022**</span></div>
  <div class="hex" role="img" aria-label="Woman on a beach" style="left:193px;top:44px;width:40px;height:35px;background:linear-gradient(180deg,#9ccbe0,#d9c6a6)"></div>
  <div class="hex gold" style="left:74px;top:72px;width:60px;height:52px"><span style="font-size:5.2px;line-height:6px;padding:0 6px">Experience Economy will be worth 12 Billion by 2023*</span></div>
  <div class="hex" role="img" aria-label="Yoga pose in nature" style="left:162px;top:65px;width:36px;height:31px;background:linear-gradient(180deg,#8ab07a,#4a6a3a)"></div>
  <div class="hex grey" style="left:138px;top:90px;width:30px;height:26px"></div>
  <div class="hex grey" style="left:188px;top:76px;width:58px;height:50px"><span style="font-size:4.6px;line-height:5.4px;padding:0 6px">Co-Living expected to grow from 6.7 Billion to 14 Billion in 2025****</span></div>
  <p class="abs" style="left:14px;top:128px;width:240px;font-size:2.2px;line-height:2.7px;color:#555">Reference<br>*Experience Economy https://trendbrief.net/experience-economy-2023<br>**E-Learning https://datapulse.io/topics/e-learning-education<br>***Personal Development https://longreads.pub/personal-growth-market<br>****Co-Living https://bizwire-daily.com/co-living-segment-report-2025</p>
  <div class="accent-bar"></div>
</section>

<!-- Governance -->
<section class="slide sm c3 r4">
  <div class="photo" role="img" aria-label="Coastal town beneath mountains" style="left:0;top:0;width:268px;height:47px;background:linear-gradient(180deg,#6f86a6 0%,#8a8a86 55%,#2f5a7a 100%)"></div>
  <h2 class="heading center" style="left:0;top:21px;width:268px;font-size:12px;color:#fff">Governance</h2>
  <svg class="abs" style="left:0;top:0" width="268" height="151" viewBox="0 0 268 151" aria-hidden="true">
    <polyline points="78,64 100,64 118,82" fill="none" stroke="#555" stroke-width=".5"/>
    <polyline points="78,101 100,101 118,96" fill="none" stroke="#555" stroke-width=".5"/>
    <polyline points="193,68 176,68 150,90" fill="none" stroke="#555" stroke-width=".5"/>
    <circle cx="133" cy="91" r="28" fill="#f6c21c"/>
    <circle cx="133" cy="91" r="19" fill="#e2e2e2"/>
    <circle cx="133" cy="91" r="15" fill="#ffffff"/>
    <circle cx="133" cy="91" r="9.5" fill="#f6c21c"/>
    <circle cx="133" cy="91" r="1.6" fill="#333"/>
  </svg>
  <span class="level" style="left:46px;top:60px">Level 1</span>
  <p class="level-note center" style="left:14px;top:70px;width:64px">Core team and Advisors set the structure and agreements.</p>
  <span class="level" style="left:46px;top:97px">Level 2</span>
  <p class="level-note center" style="left:14px;top:107px;width:64px">All investors and partners who invest over $75,000 have voting abilities on the development of each property and other important decisions.</p>
  <span class="level" style="left:193px;top:64px">Level 3</span>
  <p class="level-note" style="left:193px;top:74px;width:64px">All investors and members less than $75,000 get to vote on different proposals, such as locations of future locations, architectural designs, facilitators and workshops etc.</p>
  <div class="accent-bar" style="top:45px"></div>
</section>

<!-- Values -->
<section class="slide sm c4 r4">
  <h2 class="heading center" style="left:0;top:8px;width:268px;font-size:12px">Values</h2>
  <div class="card" style="left:6px;top:45px;width:77px;height:38px"><span class="icon"></span><h3>Community</h3><p>Having strong real relationships with likeminded people is so powerful and (You are the average of the 5 people you spend the most time with)</p></div>
  <div class="card" style="left:90px;top:45px;width:77px;height:38px"><span class="icon"></span><h3>Sustainability</h3><p>We care about the environment and think it's extremely important to reduce our environmental impact we are having on it. So our decisions will always be based on being as sustainable as possible.</p></div>
  <div class="card" style="left:176px;top:45px;width:77px;height:38px"><span class="icon"></span><h3>Healthy Living</h3><p>Majority of us come from very fast paced lives that have created unbalanced lifestyles that are not sustainable. We want to create from a place of balance, with a big focus on self care</p></div>
  <div class="card" style="left:6px;top:102px;width:77px;height:38px"><span class="icon"></span><h3>Freedom</h3><p>Without freedom we are often put in situations that cause conflict and resistance. Creating a space where everyone feels free is extremely important</p></div>
  <div class="card" style="left:90px;top:102px;width:77px;height:38px"><span class="icon"></span><h3>Growth</h3><p>We believe it's important to always grow, both personally, mentally, and spiritually. This ensures we are always improving and working towards new heights</p></div>
  <div class="card" style="left:176px;top:102px;width:77px;height:38px"><span class="icon"></span><h3>Giving Back</h3><p>Supporting the local community and giving back enables us to integrate with the locals and provide value while we are visiting their countries</p></div>
  <div class="accent-bar" style="top:40px"></div>
</section>

<!-- Sustainability -->
<section class="slide sm c1 r5">
  <div class="photo" role="img" aria-label="Thatched bamboo house among plants" style="left:0;top:0;width:87px;height:151px;background:linear-gradient(180deg,#d9d2c4 0%,#a47a48 45%,#4f6a3a 100%)"></div>
  <h2 class="heading" style="right:10px;top:8px;text-align:right;font-size:9.4px;line-height:11px">Sustainability<br>and Giving Back</h2>
  <div class="pillar-box" style="top:46px">Utilizing local natural materials and supporting the local economy.</div>
  <span class="pillar-icon" style="top:34px"></span>
  <span class="pillar-title" style="top:37px">Building and Operating Sustainably</span>
  <div class="pillar-box" style="top:85px">Each property will grow its own food using an Aquaponics system and source anything we don't grow locally.</div>
  <span class="pillar-icon" style="top:73px"></span>
  <span class="pillar-title" style="top:76px">Aquaponics</span>
  <div class="pillar-box" style="top:124px">Local engagement is extremely important to us, a % of the total fund will go towards supporting local projects that are decided by the community.</div>
  <span class="pillar-icon" style="top:111px"></span>
  <span class="pillar-title" style="top:114px">Local Community Support</span>
  <div class="accent-bar" style="top:46px"></div>
</section>

<!-- Timeline -->
<section class="slide sm c2 r5">
  <h2 class="heading center" style="left:0;top:9px;width:268px;font-size:12px">Timeline</h2>
  <span class="tl-year" style="left:14px">2020</span>
  <span class="tl-year" style="left:97px">2021</span>
  <span class="tl-year" style="left:180px">2022</span>
  <div class="abs" style="left:4px;top:44.5px;width:252px;height:1px;background:var(--gold)"></div>
  <span class="tl-dot" style="left:14px"></span>
  <span class="tl-dot" style="left:97px"></span>
  <span class="tl-dot" style="left:180px"></span>
  <div class="tl-col" style="left:14px"><b>Q1:</b>Finalize Architectural Designs<br>Finalize Build Costs<br>Onboard Partners<b>Q2:</b>Finalize Funding Round<br>Acquire Land<br>Start Build<br>Start Development of Platform<br>Launch 2021 Havenfests<b>Q3:</b>Launch Local Events<br>Launch First Course<br>Launch MVP of Platform<b>Q4:</b>Operate Local Events (November - Egypt)</div>
  <div class="tl-col" style="left:97px"><b>Q1:</b>Launch Alpha of Platform<br>Operate Second Havenfest (March - Panama)<b>Q2:</b>Grand Opening of First Property<b>Q3:</b>Fundraising For 2nd Property<br>Operate 3rd Havenfest (August - Croatia)<b>Q4:</b>Operate 4th Havenfest (November - Egypt)<br>Start Building 2nd Property</div>
  <div class="tl-col" style="left:180px"><b>Q1:</b>Operate 5th Havenfest (March - Panama)<b>Q2:</b>Celebrate 1 Year Anniversary of Bali Property<b>Q3:</b>Operate 6th Havenfest (August - Croatia)<b>Q4:</b>Grand Opening of 2nd Property<br>Operate 7th Havenfest (November - Egypt)</div>
  <div class="accent-bar" style="top:40px"></div>
</section>

<!-- Funding strategy -->
<section class="slide sm c3 r5">
  <h2 class="heading center" style="left:0;top:10px;width:268px;font-size:12px">Funding Strategy</h2>
  <div class="fund-text">
    <p>All shareholders will get access to the spaces based on the amount they invest. Everything is 100% transparent and evenly distributed.</p>
    <p>Round 1:<br>Friends/Family/Partners will get the first opportunity to get in before more institutional investment comes in.</p>
    <p>Round 2:<br>Institutional investment will have the opportunity to invest with a clear buyback model from the community buying back shares from investors providing a 15% return. (If payback does not come in investors will still have ownership of the property keeping it a safe investment)</p>
    <p>Round 3:<br>Community members can buy shares from investors transitioning ownership back to the community. (At 15% more to cover the investors interest rates)</p>
  </div>
  <table class="returns">
    <tr><td class="blank" colspan="5"></td><td colspan="3">Return Assumptions</td></tr>
    <tr><td class="blank" colspan="5"></td><td colspan="3">Nightly Rates</td></tr>
    <tr><td class="blank" colspan="5"></td><td>$100</td><td>$80</td><td>$50</td></tr>
    <tr><td>Company 1</td><td>$75,000</td><td>4.79%</td><td>420</td><td>$10,464</td><td>$41,973</td><td>$33,578</td><td>$20,986</td></tr>
    <tr><td>Attendee's</td><td>$20,000</td><td>1.28%</td><td>112</td><td>$2,791</td><td>$11,193</td><td>$8,954</td><td>$5,596</td></tr>
    <tr><td>Attendee's</td><td>$10,000</td><td>0.64%</td><td>56</td><td>$1,395</td><td>$5,596</td><td>$4,477</td><td>$2,798</td></tr>
    <tr><td>Attendee's</td><td>$5,000</td><td>0.32%</td><td>28</td><td>$698</td><td>$2,798</td><td>$2,239</td><td>$1,399</td></tr>
    <tr><td>Attendee's</td><td>$1,000</td><td>0.06%</td><td>6</td><td>$140</td><td>$560</td><td>$448</td><td>$280</td></tr>
    <tr><td class="blank" colspan="5"></td><td class="blank"></td><td class="blank"></td><td class="blank"></td></tr>
    <tr><td class="blank" colspan="5"></td><td colspan="3">Annual Return</td></tr>
    <tr><td class="blank" colspan="5"></td><td>55.96%</td><td>44.77%</td><td>27.98%</td></tr>
  </table>
  <p class="abs" style="left:93px;top:98px;width:165px;font-size:2.3px;color:#555">*Approximate Numbers based on 30 rooms x 365 nights (Minus 20% for team and facilitators) (80%) = 8760 Room nights</p>
  <div class="accent-bar" style="top:30px"></div>
</section>

<!-- Use of funds -->
<section class="slide sm c4 r5">
  <div class="photo" role="img" aria-label="Sun loungers and parasols on a rocky seaside terrace" style="left:0;top:19px;width:142px;height:111px;background:linear-gradient(180deg,#8fb0c8 0%,#4f8a5a 30%,#3f9ab8 55%,#b89a7a 100%)"></div>
  <h2 class="heading" style="left:152px;top:33px;font-size:11px">Use of Funds</h2>
  <p class="abs center" style="left:150px;top:62px;width:108px;font-size:4px;color:#444">Initial Raise: $2,000,000</p>
  <p class="abs center" style="left:150px;top:75px;width:108px;font-size:4px;color:#444">1.5M Used for Development of first Property</p>
  <p class="abs center" style="left:150px;top:89px;width:108px;font-size:4px;line-height:4.7px;color:#444">500k Used for building the community of members through a Personal Growth Marketplace for all partner companies to join and offer their services.</p>
</section>

</main>
</body>
</html>
```